Music Festival Business Cards

The Lantern Gathering
Produced by Bramblewood Sound Collective LLC
New music festival in Arkansas.

Target Market(s)

18-35 year olds

Industry/Entity Type

Festival

Contact Information for Business Card

We are a 5-partner team producing a music festival in Arkansas. We need slick business cards, and I want them to be square.

Requirements
Must have
• I NEED THESE TO BE IN SQUARE SIZE - 2x2 or 2.5x2.5... please not regular size.
• I need www.lanternmeet.example as the link to website.

```html
<!DOCTYPE html>
<html lang="en">
<head>
<meta charset="utf-8">
<title>The Lantern Gathering — Square Business Cards</title>
<link rel="stylesheet" href="https://fonts.googleapis.com/css2?family=Oswald:wght@500&family=Work+Sans:wght@400;600&display=swap">
<style>
  :root {
    --backdrop: #1b1b1c;
    --card: #121213;
    --card-edge: #232325;
    --silver: #c4c4c6;
    --silver-dim: #8a8a8d;
    --ink-muted: #55555a;
    --emboss: #3d3d41;
  }
  * { box-sizing: border-box; margin: 0; padding: 0; }
  html, body {
    width: 1200px; height: 900px; overflow: hidden;
    background: var(--backdrop);
    font-family: "Work Sans", Arial, sans-serif;
  }
  .sheet {
    width: 1200px; height: 900px;
    display: flex; align-items: center; justify-content: center; gap: 40px;
  }
  .card {
    width: 450px; height: 450px;
    background: var(--card);
    border: 1px solid var(--card-edge);
    position: relative;
  }
  .card-front {
    display: flex; flex-direction: column;
    align-items: center; justify-content: center;
  }
  .brand {
    display: flex; align-items: center; gap: 18px;
  }
  .brand-mark {
    width: 26px; height: 26px; flex: none;
    border: 2px solid var(--silver);
  }
  .brand-name {
    font-weight: 600; font-size: 30px; line-height: 1.2;
    letter-spacing: 0.12em; text-transform: uppercase;
    color: var(--silver);
  }
  .address {
    margin-top: 40px;
    font-size: 13px; color: var(--ink-muted);
    letter-spacing: 0.02em; white-space: nowrap;
  }
  .card-back {
    display: flex; align-items: center; justify-content: center;
    gap: 16px; padding: 0 18px;
  }
  .person { text-align: right; white-space: nowrap; }
  .person-name {
    font-family: "Oswald", "Arial Narrow", sans-serif;
    font-weight: 500; font-size: 24px;
    letter-spacing: 0.03em; text-transform: uppercase;
    color: var(--emboss);
    line-height: 1.1;
  }
  .person-role {
    font-size: 12px; color: var(--ink-muted);
    letter-spacing: 0.04em;
  }
  .divider {
    width: 1px; height: 54px; flex: none;
    background: var(--ink-muted);
  }
  .contacts { list-style: none; }
  .contacts li {
    display: flex; align-items: center; gap: 9px;
    font-size: 12px; color: var(--silver);
    letter-spacing: 0.03em; line-height: 1.5; white-space: nowrap;
  }
  .contacts svg {
    width: 11px; height: 11px; flex: none;
    fill: none; stroke: var(--silver-dim); stroke-width: 1.6;
  }
</style>
</head>
<body>
  <main class="sheet">
    <section class="card card-front" aria-label="Card front">
      <div class="brand">
        <span class="brand-mark" aria-hidden="true"></span>
        <span class="brand-name">The Lantern<br>Gathering</span>
      </div>
      <p class="address">418 Cedar Hollow Road Fayetteville, AR 72701</p>
    </section>

    <section class="card card-back" aria-label="Card back">
      <div class="person">
        <h1 class="person-name">Marlow Fenwick</h1>
        <p class="person-role">Director</p>
      </div>
      <span class="divider" aria-hidden="true"></span>
      <ul class="contacts">
        <li>
          <svg viewBox="0 0 16 16" aria-hidden="true"><path d="M4 2l2.5 3-1.5 1.5c1 2 2.5 3.5 4.5 4.5L11 9.5l3 2.5-1.5 2C7 13.5 2.5 9 2 3.5z"/></svg>
          479 555 0148
        </li>
        <li>
          <svg viewBox="0 0 16 16" aria-hidden="true"><rect x="1.5" y="3.5" width="13" height="9"/><path d="M1.5 3.5L8 9l6.5-5.5"/></svg>
          hello@lanternmeet.example
        </li>
        <li>
          <svg viewBox="0 0 16 16" aria-hidden="true"><circle cx="8" cy="8" r="6.5"/><ellipse cx="8" cy="8" rx="2.8" ry="6.5"/><path d="M1.5 8h13"/></svg>
          www.lanternmeet.example
        </li>
      </ul>
    </section>
  </main>
</body>
</html>
```